5 Banner für die Startseite der Hompage
Zielgruppe
Wir sind eine 'kreative' kleine Truppe, die mit neuen Ideen versuchen wollen, auch mal andere Wege in den Projekten zu gehen.
unsere neue Webseite lautet
Aufgabenstellung
Auf meiner Webseite www.kavelorn.de habe ich bereits einen ersten Vorschlag eingefügt.
Es geht um die 5 Banner auf der Startseite; diese sollen sowohl Designtechnisch als auch optisch sehr ansprechend wirken, um das Interesse potentieller Kunden zu wecken.
Meine Farben habe ich mit angehängt.
Der Text könnte sich noch anpassen, muss aber mit in den Banner aufgenommen werden.
Breite sollte 1200Pixel; Höhe 600Pixel

```html
<!DOCTYPE html>
<html lang="de">
<head>
<meta charset="utf-8">
<title>Kavelorn – Startseite</title>
<link rel="stylesheet" href="https://fonts.googleapis.com/css2?family=Fira+Sans:ital,wght@0,400;0,500;0,600;1,400&family=Lato:wght@400;900&display=swap">
<style>
  :root {
    --pink: #ee4f95;
    --pink-dark: #c23a78;
    --pink-arc: rgba(240, 100, 160, 0.75);
    --ink: #3f4a4f;
    --ink-dark: #2e3b42;
    --white: #ffffff;
    --page: #f7f7f7;
    --hero-top: #8a6460;
    --hero-mid: #7d6a72;
    --hero-bottom: #6f7484;
  }
  * { margin: 0; padding: 0; box-sizing: border-box; }
  html, body { width: 1200px; height: 606px; overflow: hidden; background: var(--page); }
  body { position: relative; font-family: "Fira Sans", sans-serif; color: var(--ink); }

  .hero {
    position: absolute; left: 0; top: 0; width: 1200px; height: 481px;
    background: linear-gradient(170deg, var(--hero-top) 0%, var(--hero-mid) 45%, var(--hero-bottom) 100%);
  }

  .site-nav {
    position: absolute; left: 0; top: 0; width: 1200px; height: 50px;
  }
  .site-nav .brand {
    position: absolute; left: 190px; top: 12px;
    font-family: "Fira Sans", sans-serif; font-weight: 600; font-size: 18px; color: var(--white);
  }
  .site-nav .menu {
    position: absolute; right: 229px; top: 17px; display: flex; gap: 14px; list-style: none;
    font-family: "Lato", sans-serif; font-size: 9px; color: var(--white);
  }

  .banner {
    position: absolute; left: 184px; top: 80px; width: 788px; height: 361px;
    background: var(--white); box-shadow: 0 6px 18px rgba(0,0,0,0.35); overflow: hidden;
  }
  .banner .photo {
    position: absolute; left: 506px; top: 0; width: 282px; height: 361px;
    background: linear-gradient(180deg, #e9eef8 0%, #d6def0 55%, #c9d2e6 100%);
  }
  .banner .arc { position: absolute; left: 0; top: 0; }
  .quote-mark {
    position: absolute; left: 26px; top: 56px;
    font-size: 78px; font-style: italic; font-weight: 600; color: var(--pink); line-height: 1;
  }
  .quote {
    position: absolute; left: 68px; top: 62px; width: 470px;
    font-size: 32px; line-height: 42px; font-weight: 400; color: var(--ink);
  }
  .quote-author {
    position: absolute; left: 0; top: 186px; width: 510px; text-align: right;
    font-size: 13px; font-style: italic; color: var(--ink);
  }
  .teaser {
    position: absolute; left: 71px; top: 275px;
    font-size: 14px; line-height: 19px; color: var(--ink);
  }
  .read-more {
    position: absolute; left: 69px; top: 320px;
    font-size: 17px; font-weight: 500; color: var(--pink); text-decoration: none;
  }
  .banner-brand {
    position: absolute; left: 697px; top: 334px;
    font-size: 18px; font-weight: 600; color: var(--ink-dark);
  }

  .slider-arrow {
    position: absolute; top: 236px; width: 33px; height: 49px; background: var(--pink);
  }
  .slider-arrow::before {
    content: ""; position: absolute; top: -12px; border-style: solid;
  }
  .slider-arrow.prev { left: 174px; }
  .slider-arrow.prev::before { right: 0; border-width: 0 0 12px 10px; border-color: transparent transparent var(--pink-dark) transparent; }
  .slider-arrow.next { left: 949px; }
  .slider-arrow.next::before { left: 0; border-width: 0 10px 12px 0; border-color: transparent transparent var(--pink-dark) transparent; }
  .slider-arrow svg { position: absolute; left: 8px; top: 14px; }

  .section-approach {
    position: absolute; left: 0; top: 481px; width: 1200px; height: 125px; background: var(--page);
  }
  .section-approach h2 {
    position: absolute; left: 0; top: 60px; width: 1200px; text-align: center;
    font-family: "Lato", sans-serif; font-weight: 900; font-size: 29px; color: var(--ink-dark); letter-spacing: 0.5px;
  }
  .section-approach .divider { position: absolute; left: 551px; top: 108px; }
</style>
</head>
<body>
  <header class="hero" role="img" aria-label="Hintergrund mit technischer Zeichnung in Rosé- und Graublau-Tönen"></header>

  <nav class="site-nav">
    <div class="brand">Kavelorn</div>
    <ul class="menu">
      <li>Home</li>
      <li>Unser Ansatz</li>
      <li>Produkte</li>
      <li>Dienstleistungen</li>
      <li>Schulungen</li>
    </ul>
  </nav>

  <section class="banner">
    <div class="photo" role="img" aria-label="Foto eines Mannes im Hemd, der sich verzweifelt die Haare rauft"></div>
    <svg class="arc" width="788" height="361" viewBox="0 0 788 361" aria-hidden="true">
      <path d="M608 361 A134 134 0 0 1 876 361 L838 361 A96 96 0 0 0 646 361 Z" fill="var(--pink-arc)"/>
    </svg>
    <div class="quote-mark">”</div>
    <p class="quote">Probleme kann man niemals mit derselben Denkweise lösen, durch die sie entstanden sind.</p>
    <p class="quote-author">Konrad Wellmer</p>
    <p class="teaser">Die Kompelixtät Ihrer System ist zum Haare raufen?<br>Sie wollen Probleme und Risiken schneller identifizieren können?</p>
    <a class="read-more" href="#">&gt;&gt; Lesen Sie mehr</a>
    <div class="banner-brand">Kavelorn</div>
  </section>

  <div class="slider-arrow prev">
    <svg width="17" height="21" viewBox="0 0 17 21" aria-hidden="true"><path d="M15 2 L3 10.5 L15 19" fill="none" stroke="#fff" stroke-width="3.5"/></svg>
  </div>
  <div class="slider-arrow next">
    <svg width="17" height="21" viewBox="0 0 17 21" aria-hidden="true"><path d="M2 2 L14 10.5 L2 19" fill="none" stroke="#fff" stroke-width="3.5"/></svg>
  </div>

  <section class="section-approach">
    <h2>UNSER ANSATZ</h2>
    <svg class="divider" width="98" height="12" viewBox="0 0 98 12" aria-hidden="true">
      <g stroke="var(--ink-dark)" stroke-width="3.2" stroke-linecap="round">
        <path d="M1 1 L10 10 M10 1 L1 10"/>
        <path d="M19 1 L28 10 M28 1 L19 10"/>
        <path d="M37 1 L46 10 M46 1 L37 10"/>
      </g>
    </svg>
  </section>
</body>
</html>
```